Velmor Partners - website for real estate investment company

Create a bold, modern website that reflects Velmor’s success, professionalism, and credibility.
The design must stand out while maintaining a polished, corporate tone. (bold, but understated)
The client just created a new logo, and the website design must be in sync with the logo design. Information about the logo colors, fonts, and message are in the attached design brief.

Target Market(s)

b2b: banks, brokers, institutional partners, vendors, and property sellers.

Industry/Entity Type

real estate investment company

Number of Pages Required

1 page

Font styles to use
Sans Serif

Colors

Designer to choose colors to be used in the design.

Requirements
Must have
• 1. homepage design (psd) 2. a top banner image (psd) for a default inner page
Nice to have
• please see attached design brief
Should not have

```html
<!DOCTYPE html>
<html lang="en">
<head>
<meta charset="utf-8">
<title>Velmor Partners</title>
<link href="https://fonts.googleapis.com/css2?family=Barlow:wght@400;500;600;700;800&display=swap" rel="stylesheet">
<style>
:root{
  --red:#e3212a;
  --ink:#111113;
  --slate:#4f4f52;
  --line:#d9d9dc;
  --muted:#8a8a8f;
  --footer:#151516;
  --white:#ffffff;
}
*{margin:0;padding:0;box-sizing:border-box}
html,body{width:803px;height:1200px;overflow:hidden;background:var(--white)}
body{position:relative;font-family:"Barlow",Arial,sans-serif;color:var(--ink)}
.abs{position:absolute}
.brand{font-weight:800;letter-spacing:.5px;line-height:1}
.site-header .brand{left:94px;top:16px;font-size:28px;color:var(--slate)}
.main-nav{left:238px;top:24px;display:flex;gap:17px;font-size:8.6px;letter-spacing:.3px;color:#222}
.btn{background:var(--slate);color:var(--white);font-weight:700;display:flex;align-items:center;justify-content:center;letter-spacing:.3px;position:absolute}
.btn::before{content:"";position:absolute;left:0;top:0;border-top:9px solid var(--red);border-right:9px solid transparent}
.btn-contact{left:632px;top:16px;width:77px;height:29px;font-size:8.5px}
.hero{left:0;top:60px;width:803px;height:373px;background:linear-gradient(180deg,#4b78c0 0%,#6b7fb9 30%,#6a6a95 55%,#3d3446 78%,#141621 100%)}
.hero-title{left:0;top:180px;width:803px;text-align:center;color:var(--white);font-size:31px;font-weight:800;letter-spacing:.4px}
.hero-text{left:130px;top:230px;width:543px;text-align:center;color:var(--white);font-size:13px;line-height:16.6px;letter-spacing:.2px}
.stat{top:391px;width:193px;height:190px;background:var(--white);box-shadow:0 6px 16px rgba(0,0,0,.06);text-align:center}
.stat svg{margin-top:21px}
.stat-num{font-size:30px;font-weight:700;margin-top:8px;line-height:1;letter-spacing:.5px}
.stat-label{font-size:11px;font-weight:700;margin-top:8px;letter-spacing:.3px}
.stat-sub{font-size:12px;margin-top:10px}
.section-title{left:0;top:632px;width:803px;text-align:center;font-size:23px;font-weight:700;letter-spacing:.5px}
.field{border:1px solid var(--line);background:var(--white);display:flex;align-items:flex-start;padding-top:12px;font-size:8.5px;color:var(--muted);position:absolute}
.field svg{margin-left:9px;flex:none}
.field span{border-left:1px solid var(--line);padding-left:8px;margin-left:8px;height:12px;line-height:12px}
.btn-submit{left:200px;top:857px;width:412px;height:36px;font-size:8.5px}
.site-footer{left:0;top:958px;width:803px;height:242px;background:var(--footer);color:var(--white)}
.site-footer .brand{left:0;top:40px;width:803px;text-align:center;font-size:32px;color:var(--white)}
.footer-nav{left:0;top:96px;width:803px;display:flex;justify-content:center;gap:17px;font-size:8.6px;letter-spacing:.3px}
.contact-item{top:136px;display:flex;gap:7px;align-items:center}
.icon-box{width:29px;height:29px;border:1px solid #3a3a3c;display:flex;align-items:center;justify-content:center}
.contact-item b{display:block;font-size:8.5px;letter-spacing:.3px}
.contact-item small{display:block;font-size:8.5px;margin-top:3px}
.btn-career{left:556px;top:136px;width:103px;height:29px;font-size:8.5px}
.footer-rule{left:94px;top:201px;width:615px;height:1px;background:#3a3a3c}
.copyright{left:94px;top:215px;font-size:8.5px}
.social{top:213px;width:17px;height:17px;border:1px solid #4a4a4d}
</style>
</head>
<body>
<header class="site-header">
  <div class="abs brand">VELMOR</div>
  <nav class="abs main-nav"><span>HOME</span><span>OUR STORY</span><span>INVESTMENT STRATEGY</span><span>WHAT SETS US APART</span><span>OUR PORTFOLIO</span></nav>
  <div class="btn btn-contact">CONTACT US</div>
</header>

<section class="abs hero" role="img" aria-label="City skyline at dusk with a tall tower against a blue sky"></section>
<h1 class="abs hero-title">EXPERIENCE - STRATEGY - VISION</h1>
<p class="abs hero-text">Velmor Partners Is A Vertically Integrated Real Estate Investment Firm With A Proven Four-Decade Track Record. We Acquire, Reposition, And Operate High-Performing Assets Across Multiple Sectors Always With A Focus On Exceptional, Risk-Adjusted Returns.</p>

<div class="abs stat" style="left:94px">
  <svg width="44" height="44" viewBox="0 0 44 44" fill="none" stroke="var(--red)" stroke-width="1.6" stroke-linejoin="round"><path d="M4 20l8-8 8 5 6-4 10 7-14 14-4-3-4 2-10-13z"/><path d="M15 28l4 4M18 25l5 5M21 22l5 5"/><path d="M22 4v5M14 6l3 4M30 6l-3 4"/></svg>
  <div class="stat-num">1989</div><div class="stat-label">FOUNDED</div><div class="stat-sub">Over 35 Years Of Excellence</div>
</div>
<div class="abs stat" style="left:305px">
  <svg width="44" height="44" viewBox="0 0 44 44" fill="none" stroke="var(--red)" stroke-width="1.6"><circle cx="16" cy="13" r="5"/><circle cx="16" cy="13" r="8" stroke-dasharray="3 2"/><path d="M26 8h6M26 13h8M26 18h6"/><circle cx="35" cy="6" r="2"/><circle cx="37" cy="13" r="2"/><circle cx="35" cy="20" r="2"/><path d="M2 34l8-6h10l4 3h8l8-4-10 10H10l-8 3z"/></svg>
  <div class="stat-num">23,000+</div><div class="stat-label">UNITS MANAGED</div><div class="stat-sub">Multifamily &amp; Healthcare</div>
</div>
<div class="abs stat" style="left:516px">
  <svg width="44" height="44" viewBox="0 0 44 44" fill="none" stroke="var(--red)" stroke-width="1.6"><path d="M17 4h10l-3 6h-4z"/><path d="M19 11c-8 4-12 12-8 20 2 4 16 4 20 0 4-8 0-16-8-20z"/><text x="22" y="28" font-size="12" text-anchor="middle" fill="var(--red)" stroke="none" font-family="Barlow,sans-serif" font-weight="700">$</text><path d="M3 28h10M3 32h10M3 36h10M3 40h10"/><rect x="32" y="26" width="9" height="14"/></svg>
  <div class="stat-num">$300M+</div><div class="stat-label">INVESTED</div><div class="stat-sub">In Property Renovations</div>
</div>

<h2 class="abs section-title">GET IN TOUCH</h2>
<form>
  <div class="field" style="left:200px;top:679px;width:201px;height:36px"><svg width="10" height="12" viewBox="0 0 10 12" fill="none" stroke="var(--red)"><circle cx="5" cy="3.5" r="2.5"/><path d="M1 11c0-3 2-4.5 4-4.5s4 1.5 4 4.5"/></svg><span>First Name</span></div>
  <div class="field" style="left:411px;top:679px;width:201px;height:36px"><svg width="10" height="12" viewBox="0 0 10 12" fill="none" stroke="var(--red)"><circle cx="5" cy="3.5" r="2.5"/><path d="M1 11c0-3 2-4.5 4-4.5s4 1.5 4 4.5"/></svg><span>Last Name</span></div>
  <div class="field" style="left:200px;top:724px;width:201px;height:36px"><svg width="11" height="12" viewBox="0 0 11 12" fill="none" stroke="var(--red)"><path d="M1 4l4.5-3 4.5 3v6H1z"/><path d="M1 4l4.5 3 4.5-3"/></svg><span>Your Email</span></div>
  <div class="field" style="left:411px;top:724px;width:201px;height:36px"><svg width="11" height="12" viewBox="0 0 11 12" fill="none" stroke="var(--red)"><path d="M2 1l2 2-1 2c1 2 2 3 4 4l2-1 2 2-2 2C4 11 0 7 0 3z"/></svg><span>Phone</span></div>
  <div class="field" style="left:200px;top:770px;width:412px;height:73px"><svg width="11" height="12" viewBox="0 0 11 12" fill="none" stroke="var(--red)"><path d="M5.5 1a4.5 4 0 1 1-2 7.5L1 10l1-2.5A4.5 4 0 0 1 5.5 1z"/><path d="M3.5 4.5h4M3.5 6.5h3"/></svg><span>Your Message</span></div>
  <div class="btn btn-submit">SUBMIT NOW</div>
</form>

<footer class="abs site-footer">
  <div class="abs brand">VELMOR</div>
  <nav class="abs footer-nav"><span>HOME</span><span>OUR STORY</span><span>INVESTMENT STRATEGY</span><span>WHAT SETS US APART</span><span>OUR PORTFOLIO</span><span>CONTACT US</span></nav>
  <div class="abs contact-item" style="left:143px"><div class="icon-box"><svg width="10" height="13" viewBox="0 0 10 13"><path d="M5 0a5 5 0 0 1 5 5c0 4-5 8-5 8S0 9 0 5a5 5 0 0 1 5-5z" fill="var(--red)"/><circle cx="5" cy="5" r="1.8" fill="var(--footer)"/></svg></div><div><b>ADDRESS</b><small>Maple Ridge, NJ</small></div></div>
  <div class="abs contact-item" style="left:271px"><div class="icon-box"><svg width="12" height="12" viewBox="0 0 12 12"><path d="M2 0l3 3-1.5 2c1 2 2 3 4 4L9 7.5l3 3-2 1.5C5 12 0 7 0 2z" fill="var(--red)"/></svg></div><div><b>PHONE</b><small>123 456 7890</small></div></div>
  <div class="abs contact-item" style="left:408px"><div class="icon-box"><svg width="12" height="10" viewBox="0 0 12 10"><rect width="12" height="10" rx="2" fill="var(--red)"/><path d="M1 2l5 3.5L11 2" stroke="var(--footer)" fill="none"/></svg></div><div><b>EMAIL</b><small>info@velmor.com</small></div></div>
  <div class="btn btn-career">CAREER INQUIRIES</div>
  <div class="abs footer-rule"></div>
  <div class="abs copyright">© 2025 Velmor. All Rights Reserved.</div>
  <div class="abs social" style="left:622px"></div>
  <div class="abs social" style="left:645px"></div>
  <div class="abs social" style="left:668px"></div>
  <div class="abs social" style="left:691px"></div>
</footer>
</body>
</html>
```